Lumora Business Card Design

hello,
we are looking for a business card design for our Fintech Company. We are credit card processing company that is also expanding in to the crypto market. We will be focusing on crypto processing, with a crypto wallet and crypto exchange. We like the purple in the logo. We want something modern and sophisticated but at the same time simple and trust worthy to work with banks.

Industry/Entity Type

Fintech

Logo Text

Lumora

```html
<!DOCTYPE html>
<html lang="en">
<head>
<meta charset="utf-8">
<title>Lumora Business Card</title>
<link rel="stylesheet" href="https://fonts.googleapis.com/css2?family=Days+One&display=swap">
<style>
  :root {
    --page-bg: #e9e6ec;
    --card-black: #0b050d;
    --card-plum: #3a0f42;
    --card-plum-deep: #22082a;
    --brand-purple: #9a35ad;
    --rule-purple: #6d2a7c;
    --gold: #e9c24c;
    --gold-dark: #b8892a;
    --icon-ink: #3a2410;
  }
  * { margin: 0; padding: 0; box-sizing: border-box; }
  html, body {
    width: 1200px;
    height: 2486px;
    overflow: hidden;
    background: var(--page-bg);
  }
  .canvas {
    position: relative;
    width: 1200px;
    height: 2486px;
    display: flex;
    align-items: center;
    justify-content: center;
  }
  .business-card {
    position: relative;
    width: 1050px;
    height: 600px;
    overflow: hidden;
    background: var(--card-black);
    box-shadow: 0 20px 50px rgba(20, 5, 25, 0.25);
  }
  .card-pattern {
    position: absolute;
    inset: 0;
    background:
      radial-gradient(ellipse 55% 60% at 18% 88%, var(--card-plum) 0%, transparent 70%),
      radial-gradient(ellipse 45% 70% at 88% 70%, var(--card-plum) 0%, transparent 75%),
      linear-gradient(135deg, var(--card-black) 0%, var(--card-plum-deep) 45%, var(--card-black) 58%, var(--card-plum-deep) 100%);
  }
  .brand {
    position: absolute;
    left: 420px;
    top: 86px;
    font-family: "Days One", sans-serif;
    font-size: 92px;
    line-height: 1;
    color: var(--brand-purple);
    letter-spacing: 1px;
  }
  .brand-rule {
    position: absolute;
    left: 400px;
    top: 206px;
    width: 480px;
    height: 3px;
    background: var(--rule-purple);
  }
  .contact-icons {
    position: absolute;
    right: 44px;
    top: 215px;
    display: flex;
    flex-direction: column;
    gap: 22px;
    list-style: none;
  }
  .contact-icon {
    width: 44px;
    height: 44px;
    border-radius: 50%;
    background: radial-gradient(circle at 35% 30%, #fbe08a 0%, var(--gold) 50%, var(--gold-dark) 100%);
    display: flex;
    align-items: center;
    justify-content: center;
  }
  .contact-icon svg { width: 24px; height: 24px; }
</style>
</head>
<body>
<main class="canvas">
  <section class="business-card" aria-label="Lumora business card, front">
    <div class="card-pattern" role="img" aria-label="Dark purple background with a rounded tile grid pattern"></div>
    <h1 class="brand">Lumora</h1>
    <div class="brand-rule"></div>
    <ul class="contact-icons" aria-label="Contact icons">
      <li class="contact-icon" aria-label="Address">
        <svg viewBox="0 0 24 24" fill="none" stroke="var(--icon-ink)" stroke-width="2" stroke-linejoin="round"><path d="M3 11 L12 3 L21 11"/><path d="M6 9 V20 H18 V9"/><path d="M10 20 V14 H14 V20"/></svg>
      </li>
      <li class="contact-icon" aria-label="Phone">
        <svg viewBox="0 0 24 24" fill="none" stroke="var(--icon-ink)" stroke-width="2" stroke-linejoin="round"><rect x="7" y="3" width="10" height="18" rx="2"/><path d="M11 18 H13"/></svg>
      </li>
      <li class="contact-icon" aria-label="Email">
        <svg viewBox="0 0 24 24" fill="none" stroke="var(--icon-ink)" stroke-width="2" stroke-linejoin="round"><rect x="3" y="6" width="18" height="12" rx="1"/><path d="M3 7 L12 13 L21 7"/></svg>
      </li>
      <li class="contact-icon" aria-label="Website">
        <svg viewBox="0 0 24 24" fill="none" stroke="var(--icon-ink)" stroke-width="2"><circle cx="12" cy="12" r="9"/><ellipse cx="12" cy="12" rx="4" ry="9"/><path d="M3 12 H21"/></svg>
      </li>
    </ul>
  </section>
</main>
</body>
</html>
```